Carrowind Year 9 Curriculum Model

We need a graphic that communicates all the overlapping elements of our new curriculum. Perhaps it could involve a series of concentric circles moving out from the centre:
1. the "Ideal Learner" profile at the centre with the school's logo behind it (see uploaded file).
2. The words of the "General Capabilities" from the Australian national curriculum in the next circle moving out of centre: "Ethical Understanding" "Literacy" "Numeracy" "Intercultural Awareness" "ICT Capacity" "Critical and Creative Thinking" "Personal and Social Capability"
3. Next circle out has the subjects: "Mathematics" "English" "Languages" "Health and Physical Education" "Technology" "Religious Education" "Humanities" "Arts" "Science"
4. Next Circle out has the title "Community" and then less important, the words "Local" "Regional" "National"
5. Next circle out is simple called "World"
6. Next circle out is simply called "Future"
IF there is a way to make it look not too bad...:Overlaying all the other aspects, floating somewhere, are the 3 significant priorities for the curriculum: Asia, Indigenous Culture and Sustainability

Target Market(s)

Year 9 (15 year old) school students and their parents, as well as teachers and other visitors to the school. It will be used to explain the curriculum and have on the walls as a reminder.

Industry/Entity Type

School

Requirements
Must have
• All of the words in the brief, with a relational dimension for each.

```html
<!DOCTYPE html>
<html lang="en">
<head>
<meta charset="utf-8">
<title>Carrowind Year 9 Curriculum Model</title>
<link rel="stylesheet" href="https://fonts.googleapis.com/css2?family=Nunito:wght@600;700;800&display=swap">
<style>
  :root {
    --bg: #000000;
    --ring-future: #7d3c8c;
    --ring-world: #1f6fb2;
    --ring-community: #f2a33a;
    --ring-subjects: #1d7a6b;
    --ring-capabilities: #4b2e83;
    --core: #b5d334;
    --core-text: #8e1466;
    --ring-edge: rgba(255, 255, 255, 0.35);
    --label-light: #ffffff;
    --label-soft: #fff3dc;
    --label-lavender: #ece2f7;
    --priority-fill: rgba(255, 255, 255, 0.82);
    --priority-edge: #ffffff;
    --priority-asia: #5a1a6e;
    --priority-sustain: #c93a12;
    --priority-indigenous: #135a40;
  }
  html, body {
    margin: 0;
    padding: 0;
    width: 1200px;
    height: 1000px;
    overflow: hidden;
    background: var(--bg);
  }
  .curriculum-model {
    display: block;
    width: 1200px;
    height: 1000px;
  }
  .ring { stroke: var(--ring-edge); stroke-width: 1.5; }
  .ring--future { fill: var(--ring-future); }
  .ring--world { fill: var(--ring-world); }
  .ring--community { fill: var(--ring-community); }
  .ring--subjects { fill: var(--ring-subjects); }
  .ring--capabilities { fill: var(--ring-capabilities); }
  .ring--core { fill: var(--core); }

  .label {
    font-family: "Nunito", sans-serif;
    font-weight: 600;
    text-anchor: middle;
  }
  .label--realm {
    font-size: 23px;
    font-weight: 700;
    letter-spacing: 4px;
    fill: var(--label-soft);
  }
  .label--scope {
    font-size: 13px;
    letter-spacing: 0.5px;
    fill: var(--label-soft);
  }
  .label--subject {
    font-size: 14px;
    fill: var(--label-light);
  }
  .label--capability {
    font-size: 13.5px;
    fill: var(--label-lavender);
  }
  .core-title {
    font-family: "Nunito", sans-serif;
    font-weight: 800;
    font-size: 20px;
    letter-spacing: 0.5px;
    fill: var(--core-text);
    text-anchor: middle;
  }
  .priority-badge__body {
    fill: var(--priority-fill);
    stroke: var(--priority-edge);
    stroke-width: 3;
  }
  .priority-badge__label {
    font-family: "Nunito", sans-serif;
    font-weight: 800;
    font-size: 15px;
    letter-spacing: 0.5px;
    text-anchor: middle;
  }
  .priority-badge--asia .priority-badge__label { fill: var(--priority-asia); }
  .priority-badge--sustainability .priority-badge__label { fill: var(--priority-sustain); }
  .priority-badge--indigenous .priority-badge__label { fill: var(--priority-indigenous); }
</style>
</head>
<body>
<svg class="curriculum-model" viewBox="0 0 1200 1000" xmlns="http://www.w3.org/2000/svg" role="img" aria-label="Carrowind Year 9 curriculum model: concentric circles from the Ideal Learner outward to Future">
  <defs>
    <path id="cw-90"  d="M600,590 A90 90 0 1 1 600,410 A90 90 0 1 1 600,590"/>
    <path id="cw-92"  d="M600,592 A92 92 0 1 1 600,408 A92 92 0 1 1 600,592"/>
    <path id="cw-118" d="M600,618 A118 118 0 1 1 600,382 A118 118 0 1 1 600,618"/>
    <path id="cw-122" d="M600,622 A122 122 0 1 1 600,378 A122 122 0 1 1 600,622"/>
    <path id="cw-162" d="M600,662 A162 162 0 1 1 600,338 A162 162 0 1 1 600,662"/>
    <path id="cw-180" d="M600,680 A180 180 0 1 1 600,320 A180 180 0 1 1 600,680"/>
    <path id="cw-185" d="M600,685 A185 185 0 1 1 600,315 A185 185 0 1 1 600,685"/>
    <path id="cw-192" d="M600,692 A192 192 0 1 1 600,308 A192 192 0 1 1 600,692"/>
    <path id="cw-198" d="M600,698 A198 198 0 1 1 600,302 A198 198 0 1 1 600,698"/>
    <path id="cw-250" d="M600,750 A250 250 0 1 1 600,250 A250 250 0 1 1 600,750"/>
    <path id="cw-255" d="M600,755 A255 255 0 1 1 600,245 A255 255 0 1 1 600,755"/>
    <path id="cw-325" d="M600,825 A325 325 0 1 1 600,175 A325 325 0 1 1 600,825"/>

    <path id="ccw-95"  d="M600,405 A95 95 0 1 0 600,595 A95 95 0 1 0 600,405"/>
    <path id="ccw-118" d="M600,382 A118 118 0 1 0 600,618 A118 118 0 1 0 600,382"/>
    <path id="ccw-125" d="M600,375 A125 125 0 1 0 600,625 A125 125 0 1 0 600,375"/>
    <path id="ccw-190" d="M600,310 A190 190 0 1 0 600,690 A190 190 0 1 0 600,310"/>
    <path id="ccw-200" d="M600,300 A200 200 0 1 0 600,700 A200 200 0 1 0 600,300"/>
    <path id="ccw-262" d="M600,238 A262 262 0 1 0 600,762 A262 262 0 1 0 600,238"/>
    <path id="ccw-416" d="M600,84 A416 416 0 1 0 600,916 A416 416 0 1 0 600,84"/>
  </defs>

  <g class="rings">
    <circle class="ring ring--future" cx="600" cy="500" r="445"/>
    <circle class="ring ring--world" cx="600" cy="500" r="370"/>
    <circle class="ring ring--community" cx="600" cy="500" r="295"/>
    <circle class="ring ring--subjects" cx="600" cy="500" r="222"/>
    <circle class="ring ring--capabilities" cx="600" cy="500" r="148"/>
    <circle class="ring ring--core" cx="600" cy="500" r="75"/>
  </g>

  <g class="core">
    <text class="core-title" x="600" y="478">Ideal</text>
    <text class="core-title" x="600" y="504">Carrowind</text>
    <text class="core-title" x="600" y="530">Learner</text>
  </g>

  <g class="capabilities">
    <text class="label label--capability"><textPath href="#cw-118" startOffset="60.6%">ICT Capacity</textPath></text>
    <text class="label label--capability"><textPath href="#cw-90" startOffset="68.1%">Ethical Understanding</textPath></text>
    <text class="label label--capability"><textPath href="#ccw-118" startOffset="66.7%">Critical and Creative Thinking</textPath></text>
    <text class="label label--capability"><textPath href="#ccw-95" startOffset="50%">Literacy</textPath></text>
    <text class="label label--capability"><textPath href="#ccw-125" startOffset="38.3%">Numeracy</textPath></text>
    <text class="label label--capability"><textPath href="#cw-92" startOffset="28.6%">Personal and Social Capability</textPath></text>
    <text class="label label--capability"><textPath href="#cw-122" startOffset="34.7%">Intercultural Awareness</textPath></text>
  </g>

  <g class="subjects">
    <text class="label label--subject"><textPath href="#cw-192" startOffset="51.4%">Technology</textPath></text>
    <text class="label label--subject"><textPath href="#cw-185" startOffset="63.9%">Mathematics</textPath></text>
    <text class="label label--subject"><textPath href="#cw-180" startOffset="76.4%">Religious Education</textPath></text>
    <text class="label label--subject"><textPath href="#ccw-190" startOffset="61.1%">Languages</textPath></text>
    <text class="label label--subject"><textPath href="#ccw-200" startOffset="50%">Humanities</textPath></text>
    <text class="label label--subject"><textPath href="#ccw-190" startOffset="38.6%">English</textPath></text>
    <text class="label label--subject"><textPath href="#cw-180" startOffset="19.2%">Arts</textPath></text>
    <text class="label label--subject"><textPath href="#cw-162" startOffset="36.1%">Health and Physical Education</textPath></text>
    <text class="label label--subject"><textPath href="#cw-198" startOffset="34.2%">Science</textPath></text>
  </g>

  <g class="community">
    <text class="label label--realm"><textPath href="#cw-250" startOffset="50%">COMMUNITY</textPath></text>
    <text class="label label--scope"><textPath href="#cw-255" startOffset="24.4%">National</textPath></text>
    <text class="label label--scope"><textPath href="#cw-255" startOffset="75%">Local</textPath></text>
    <text class="label label--scope"><textPath href="#ccw-262" startOffset="50%">Regional</textPath></text>
  </g>

  <g class="world">
    <text class="label label--realm"><textPath href="#cw-325" startOffset="36.7%">WORLD</textPath></text>
  </g>

  <g class="future">
    <text class="label label--realm"><textPath href="#ccw-416" startOffset="63.9%">FUTURE</textPath></text>
  </g>

  <g class="priorities">
    <g class="priority-badge priority-badge--asia">
      <circle class="priority-badge__body" cx="880" cy="262" r="62"/>
      <text class="priority-badge__label" x="880" y="268">ASIA</text>
    </g>
    <g class="priority-badge priority-badge--sustainability">
      <circle class="priority-badge__body" cx="222" cy="590" r="78"/>
      <text class="priority-badge__label" x="222" y="596">SUSTAINABILITY</text>
    </g>
    <g class="priority-badge priority-badge--indigenous">
      <circle class="priority-badge__body" cx="405" cy="838" r="72"/>
      <text class="priority-badge__label" x="405" y="834">INDIGENOUS</text>
      <text class="priority-badge__label" x="405" y="855">CULTURE</text>
    </g>
  </g>
</svg>
</body>
</html>
```